Cover for Where the Quiet River Bends Beyond Our Morning

Cover for a book that describes everything that happens to a person, from pre-birth life plans through growing in compassion and wisdom to death and living in the afterlife. The information is revealed in messages from people living in the life after this life. The title is Lanterns Along the Hidden Stair of Every Soul: Gathered from Voices Dwelling in the Further Meadow. Author is T. Morven Ashdale. Book size is 6 by 9.

Target Market(s)

General

Font styles to use
Serif

```html
<!DOCTYPE html>
<html lang="en">
<head>
<meta charset="utf-8">
<title>Lanterns Along the Hidden Stair of Every Soul — Cover</title>
<link rel="stylesheet" href="https://fonts.googleapis.com/css2?family=Great+Vibes&family=Lato:wght@400;700&family=Cormorant+Garamond:wght@500&display=swap">
<style>
  :root {
    --page-bg: #dcdcd9;
    --cover-dark: #0b0814;
    --ember: #e8823a;
    --flame: #b8322a;
    --gold: #f4c77a;
    --violet: #8a6ad8;
    --indigo: #2a2a6a;
    --teal: #3aa6b8;
    --title-ink: #f6f0f8;
    --author-ink: #f0c9a8;
  }
  * { margin: 0; padding: 0; box-sizing: border-box; }
  html, body {
    width: 1200px; height: 1200px; overflow: hidden;
    background: var(--page-bg);
  }
  .cover {
    position: absolute;
    left: 293px; top: 140px;
    width: 614px; height: 920px;
    overflow: hidden;
    background: var(--cover-dark);
  }
  .cover-art {
    position: absolute; inset: 0;
    background:
      radial-gradient(ellipse 30% 22% at 22% 66%, rgba(255,214,140,.85), transparent 70%),
      radial-gradient(ellipse 42% 40% at 20% 55%, rgba(232,130,58,.75), transparent 72%),
      radial-gradient(ellipse 38% 36% at 30% 28%, rgba(184,50,42,.7), transparent 70%),
      radial-gradient(ellipse 22% 26% at 48% 52%, rgba(58,166,184,.55), transparent 72%),
      radial-gradient(ellipse 40% 42% at 66% 40%, rgba(138,106,216,.75), transparent 72%),
      radial-gradient(ellipse 45% 50% at 80% 60%, rgba(42,42,106,.8), transparent 75%),
      linear-gradient(180deg, #120a1c 0%, #1a0f24 45%, #0b0814 100%);
  }
  .cover-shade {
    position: absolute; inset: 0;
    background: linear-gradient(180deg, rgba(8,6,14,.55) 0%, transparent 18%, transparent 72%, rgba(8,6,14,.85) 100%);
  }
  .title-script {
    position: absolute;
    left: 40px; top: 330px;
    width: 540px;
    text-align: center;
    font-family: "Great Vibes", cursive;
    font-size: 150px;
    line-height: 1;
    color: var(--title-ink);
    opacity: .92;
  }
  .subtitle {
    position: absolute;
    left: 150px; top: 526px;
    width: 430px;
    text-align: center;
    font-family: "Lato", sans-serif;
    font-size: 23px;
    line-height: 28px;
    color: var(--title-ink);
  }
  .subtitle-source {
    position: absolute;
    left: 150px; top: 588px;
    width: 430px;
    text-align: center;
    font-family: "Lato", sans-serif;
    font-weight: 700;
    font-size: 12.5px;
    color: var(--title-ink);
  }
  .author {
    position: absolute;
    left: 0; top: 818px;
    width: 614px;
    text-align: center;
    font-family: "Cormorant Garamond", serif;
    font-weight: 500;
    font-size: 27px;
    letter-spacing: 12px;
    color: var(--author-ink);
  }
</style>
</head>
<body>
  <main class="cover">
    <div class="cover-art" role="img" aria-label="Swirling luminous smoke, warm orange and red on the left blending into violet and blue on the right, around a dark glowing form"></div>
    <div class="cover-shade"></div>
    <h1 class="title-script">Lanterns</h1>
    <p class="subtitle">along the hidden stair<br>of every soul.</p>
    <p class="subtitle-source">Gathered from Voices Dwelling in the Further Meadow.</p>
    <p class="author">T. MORVEN ASHDALE</p>
  </main>
</body>
</html>
```